Business Card Design Project

we need a business card design for our company: www.plomvik.ch
It's important to include our already existing logo (see website)

```html
<!DOCTYPE html>
<html lang="de">
<head>
<meta charset="utf-8">
<title>Plomvik – Visitenkarte</title>
<link rel="stylesheet" href="https://fonts.googleapis.com/css2?family=Source+Sans+3:wght@400;600;700&display=swap">
<style>
  :root {
    --bg: #e9e6e1;
    --card-white: #ffffff;
    --brand-dark: #1d6394;
    --brand-light: #7aa0d2;
    --text-dark: #2f3a44;
    --text-muted: #55606a;
  }
  * { box-sizing: border-box; margin: 0; padding: 0; }
  html, body { width: 1200px; height: 900px; overflow: hidden; }
  body {
    background: var(--bg);
    font-family: "Source Sans 3", Arial, sans-serif;
    position: relative;
  }
  .card {
    position: absolute;
    top: 294px;
    width: 552px;
    height: 314px;
    border-radius: 20px;
    overflow: hidden;
    box-shadow: 0 4px 14px rgba(0,0,0,0.18);
  }
  .card--front { left: 33px; background: var(--card-white); }
  .card--back { left: 622px; background: var(--brand-light); }
  .card__wave { position: absolute; left: 0; top: 0; width: 552px; height: 314px; }

  .person { position: absolute; left: 38px; top: 40px; }
  .person__name { font-size: 23px; font-weight: 700; color: var(--brand-dark); }
  .person__role { font-size: 17px; color: var(--text-dark); position: relative; top: 6px; }

  .address { position: absolute; left: 38px; top: 95px; font-size: 15px; line-height: 20px; color: var(--text-muted); }
  .address__company { font-weight: 700; color: var(--text-dark); }

  .contacts { position: absolute; left: 38px; top: 178px; list-style: none; font-size: 15px; color: var(--text-muted); }
  .contacts li { display: flex; align-items: center; height: 21px; }
  .contacts svg { width: 14px; height: 12px; margin-right: 9px; fill: var(--brand-dark); }

  .wordmark { position: absolute; font-weight: 700; letter-spacing: -1px; line-height: 1; }
  .wordmark--front { left: 258px; top: 118px; font-size: 56px; color: var(--brand-dark); }
  .wordmark--back { left: 0; width: 100%; text-align: center; top: 112px; font-size: 70px; color: var(--card-white); }

  .website {
    position: absolute; left: 0; width: 100%; top: 212px;
    text-align: center; font-size: 15px; letter-spacing: 4.5px; color: var(--card-white);
  }
</style>
</head>
<body>
  <section class="card card--front">
    <svg class="card__wave" viewBox="0 0 552 314" aria-hidden="true">
      <path d="M0,250 Q270,300 552,240 L552,254 Q270,314 0,262 Z" fill="var(--brand-light)"/>
      <path d="M0,268 Q270,318 552,260 L552,314 L0,314 Z" fill="var(--brand-dark)"/>
    </svg>
    <div class="person">
      <span class="person__name">Marco Brunner</span><span class="person__role">/CEO</span>
    </div>
    <div class="address">
      <div class="address__company">Plomvik AG</div>
      <div>Talackerweg 18</div>
      <div>8045 Zürich</div>
    </div>
    <ul class="contacts">
      <li><svg viewBox="0 0 14 12"><rect x="0" y="8" width="3" height="4"/><rect x="4" y="5" width="3" height="7"/><rect x="8" y="2" width="3" height="10"/></svg>0331 74 90210</li>
      <li><svg viewBox="0 0 14 12"><path d="M1,4 Q7,-1 13,4 L11,6 L9,4 L5,4 L3,6 Z M3,7 L11,7 L12,12 L2,12 Z"/></svg>044 710 33 44</li>
      <li><svg viewBox="0 0 14 12"><path d="M0,1 L14,1 L14,11 L0,11 Z M1.5,2.5 L7,7 L12.5,2.5" fill="none" stroke="var(--brand-dark)" stroke-width="1.6"/></svg>info@plomvik.ch</li>
    </ul>
    <div class="wordmark wordmark--front">Plomvik</div>
  </section>

  <section class="card card--back">
    <svg class="card__wave" viewBox="0 0 552 314" aria-hidden="true">
      <path d="M0,258 Q270,318 552,248 L552,314 L0,314 Z" fill="var(--brand-dark)"/>
    </svg>
    <div class="wordmark wordmark--back">Plomvik</div>
    <div class="website">www.plomvik.ch</div>
  </section>
</body>
</html>
```